WordPress Blog/Website for Athlete Focused Sports Marketing Agency

WordPress Website that Serves two primary purposes:

1) Company Information Website which showcases organization's capabilities and work

2) Highlights, Showcases and Displays key information for athlete clients, aggregates all of the content they are creating(mostly social) and is a key portal for publishing press releases, news updates and more.

Key Criteria for Success:

Easily Updatable
Easy to Navigate
Clean Design that follows the function/form of the organization's brand identity while also incorporating the identity of the athletes.

Supporting Documentation:**These files are also uploaded and attached to this project description**
Creative Brief: https://files.vorteldrive.net/a/lumbrecrest.com/file/d/7Kx2PqRmWtZ4nJvLbHsYcEgAoUi/edit?usp=sharing
Logo Files/Designs are attached. Color Palette can be adjusted as necessary.

WireFrame: (Please use your own judgement and creative liberty's to make something that is a lot better then what I came up with):
https://files.vorteldrive.net/file/d/7Kx2PqRmWtZ4mBcNdFgHjKlQwEr/edit?usp=sharing

Current Website(Incomplete): www.lumbrecrest.com

Thanks!

Industry/Entity Type

It Company

Requirements
Must have
• Social Media Integration: A social feed that aggregates content across all channels for multiple users(all of my athletes)

"News=Blog" Portal that serves as the primary engine for the page's content

Professional Look and Design- it should look like a website, not a blog.

```html
<!DOCTYPE html>
<html lang="en">
<head>
<meta charset="utf-8">
<title>Lumbre Crest Media Group</title>
<link rel="stylesheet" href="https://fonts.googleapis.com/css2?family=Arimo:wght@400;700&family=Crimson+Text:wght@400;600&display=swap">
<style>
:root{
  --orange:#f57f10;
  --orange-light:#fca443;
  --orange-text:#e8650f;
  --bg:#f7f7f7;
  --panel:#ffffff;
  --card:#f1f1f1;
  --bar-top:#5a5a5a;
  --bar-bottom:#2c2c2c;
  --text:#333333;
  --muted:#666666;
  --link:#1f7fa8;
  --link-red:#b42012;
  --navy:rgba(20,30,48,.93);
  --sky:#3d78b5;
}
*{box-sizing:border-box;margin:0;padding:0}
html,body{width:1200px;height:1144px;overflow:hidden}
body{background:var(--bg);font-family:"Arimo",Arial,sans-serif;color:var(--text);position:relative}
.site{position:absolute;left:90px;top:0;width:1020px}

/* header */
.masthead{height:104px;position:relative}
.brand{position:absolute;left:0;top:21px;display:flex;align-items:center;gap:8px}
.brand-mark{width:62px;height:62px;border-radius:50%;background:var(--orange)}
.brand-name{font-family:"Crimson Text",Georgia,serif;font-size:32px;color:var(--orange);line-height:1}
.search{position:absolute;left:757px;top:38px;width:169px;height:29px;background:#fff;border:1px solid #cfcfcf;font-size:11px;color:#333;padding:8px 12px}
.search svg{position:absolute;right:8px;top:6px}
.lang{position:absolute;left:936px;top:38px;width:84px;height:29px;background:#fff;border:1px solid #cfcfcf;font-size:11px;padding:7px 8px;display:flex;align-items:center;gap:6px}
.lang .flag{width:16px;height:11px;background:#3b4f8a}
.lang svg{margin-left:10px}

/* navigation */
.nav{height:50px;background:linear-gradient(var(--orange-light),var(--orange));display:flex;align-items:stretch;position:relative}
.nav a{color:#fff;text-decoration:none;font-weight:700;font-size:13px;display:flex;align-items:center;padding:0 24px;border-right:1px solid #e16c06;box-shadow:1px 0 0 #ffb566}
.nav a.active{background:linear-gradient(#ffc07a,#fa9430)}
.social{position:absolute;right:12px;top:9px;display:flex;gap:14px}
.social span{width:33px;height:33px;border-radius:50%;background:#fff;display:block}

/* slider */
.slider{margin-top:10px;height:394px;background:#e3e3e3;border:1px solid #d2d2d2;padding:11px 8px}
.slide{height:372px;background:linear-gradient(180deg,#2f66a8,#5b97d2 65%,#8bb7e2);position:relative}
.slide-photo{position:absolute;right:0;top:0;width:520px;height:372px;background:radial-gradient(ellipse at 55% 60%,#c8312c 0,#a8342f 28%,rgba(70,110,170,0) 60%)}
.news-box{position:absolute;left:28px;top:66px;width:399px;height:248px;background:var(--navy);color:#fff;padding:18px 18px}
.news-box h2{font-size:21px;font-weight:700;padding-bottom:13px;border-bottom:1px solid #6b7482;letter-spacing:.2px}
.news-box h3{font-size:17px;font-weight:700;line-height:25px;margin-top:14px;color:#e8e8e8;text-align:justify}
.news-box p{font-size:13px;line-height:23px;margin-top:8px;color:#e0e0e0;text-align:justify}
.news-box .meta{font-size:13px;color:#aab0b8;margin-top:8px}
.dots{position:absolute;right:30px;bottom:30px;display:flex;gap:9px}
.dots i{width:16px;height:16px;border-radius:50%;background:#7f9cc0;border:2px solid #d8e2ee;display:block}
.dots i.on{background:#fff}

/* content */
.content{margin-top:18px;height:447px;background:var(--panel);border:1px solid #dddddd;position:relative}
.section-title{font-family:"Crimson Text",Georgia,serif;font-size:27px;color:var(--orange-text);position:absolute;top:18px;font-weight:400}
.bar{position:absolute;top:62px;height:52px;background:linear-gradient(var(--bar-top),var(--bar-bottom));display:flex;align-items:center;padding-left:20px;font-family:"Crimson Text",Georgia,serif;font-size:19px;color:#fff}
.bar .arrow{position:absolute;right:16px;top:16px;width:19px;height:19px;border-radius:50%;background:#ddd;display:flex;align-items:center;justify-content:center}
.bar .tab{color:#a9a9a9}
.bar .sep{color:#a9a9a9;margin:0 14px;font-size:16px}

.buzz{position:absolute;left:14px;top:0;width:287px}
.tweets{position:absolute;top:118px;left:0;width:287px;display:flex;flex-direction:column;gap:5px}
.tweet{height:99px;background:var(--card);padding:11px 12px 0 57px;position:relative;font-size:12px;line-height:20px}
.tweet .avatar{position:absolute;left:11px;top:12px;width:36px;height:36px;background:#8d6a55;border:2px solid #fff;box-shadow:0 0 1px #999}
.tweet .avatar.square{background:#3fb0d9}
.tweet a{color:var(--link);text-decoration:none}
.tweet a.ext{color:var(--link-red);text-decoration:underline}
.tweet .actions{font-size:9.5px;color:var(--link)}

.latest{position:absolute;left:320px;top:0;width:683px}
.grid{position:absolute;top:118px;left:0;width:683px;display:grid;grid-template-columns:338px 338px;gap:5px 7px}
.card{height:99px;background:var(--card);position:relative;padding:11px 10px 0 129px;font-size:12px;line-height:18px}
.card .thumb{position:absolute;left:12px;top:11px;width:95px;height:76px;border:3px solid #fff;box-shadow:0 0 2px #999}
.card h4{font-weight:400;color:var(--orange-text);font-size:13px;margin-bottom:6px}
.card .date{color:#555;margin-top:1px}

/* footer */
.footer{margin-top:25px;position:relative;font-size:13.5px;color:#444}
.footer nav a{color:#444;text-decoration:none}
.footer nav .pipe{margin:0 10px}
.footer .copy{margin-top:17px}
.footer .brand-small{position:absolute;right:0;top:10px;display:flex;align-items:center;gap:6px;font-family:"Crimson Text",Georgia,serif;font-size:20px;color:#999}
.footer .brand-small i{width:40px;height:40px;border-radius:50%;background:#a5a5a5;display:block}
</style>
</head>
<body>
<div class="site">
  <header class="masthead">
    <div class="brand"><span class="brand-mark"></span><span class="brand-name">Lumbre Crest</span></div>
    <div class="search">Search
      <svg width="17" height="17" viewBox="0 0 17 17"><circle cx="6.5" cy="6.5" r="5" fill="#222"/><path d="M10 10l5 5" stroke="#222" stroke-width="3" stroke-linecap="round"/></svg>
    </div>
    <div class="lang"><span class="flag" role="img" aria-label="English flag"></span>Eng
      <svg width="10" height="6" viewBox="0 0 10 6"><path d="M0 0h10L5 6z" fill="#333"/></svg>
    </div>
  </header>

  <nav class="nav">
    <a class="active" href="#">HOME</a>
    <a href="#">WHAT WE DO</a>
    <a href="#">ATHLETES</a>
    <a href="#">NEWS</a>
    <a href="#">CONTACT US</a>
    <div class="social" aria-label="Social links"><span></span><span></span><span></span></div>
  </nav>

  <section class="slider">
    <div class="slide">
      <div class="slide-photo" role="img" aria-label="Cyclist in red jersey drinking from a bottle against blue sky"></div>
      <article class="news-box">
        <h2>LATEST NEWS</h2>
        <h3>Sed placerat arcu quis arcu semper, nec tincidunt nibh molestie</h3>
        <p>Interdum et malesuada fames ac ante ipsum primis in faucibus. Aliquam gravida at nisi eu tempor. In sit amet nisi in augue cursus faucibus.</p>
        <div class="meta">Jun-17-2013 &nbsp; | &nbsp; Category : Tournament</div>
      </article>
      <div class="dots"><i class="on"></i><i></i><i></i><i></i></div>
    </div>
  </section>

  <main class="content">
    <section class="buzz">
      <h2 class="section-title">The Buzz</h2>
      <div class="bar" style="width:287px">Recent Tweets
        <span class="arrow"><svg width="8" height="9" viewBox="0 0 8 9"><path d="M2 1l4 3.5L2 8" stroke="#333" stroke-width="1.8" fill="none"/></svg></span>
      </div>
      <div class="tweets">
        <div class="tweet"><span class="avatar square" role="img" aria-label="Account avatar"></span>
          <a href="#">https://chirpline.net/marenolsetri</a><br>tenetur a volup tatibus maiores alias<br><a class="ext" href="#">http://www.incidunt.com/ ut/labore/4et</a><br><span class="actions">2 minutes ago · reply · retweet · favorite</span></div>
        <div class="tweet"><span class="avatar" role="img" aria-label="Runners on a track"></span>
          <a href="#">chirpline.net/tovarunetri</a><br>tenetur a volup tatibus maiores alias<br><a class="ext" href="#">http://www.incidunt.com/ ut/labore/4et</a><br><span class="actions">2 minutes ago · reply · retweet · favorite</span></div>
        <div class="tweet"><span class="avatar" style="background:#a4493a" role="img" aria-label="Sprinters racing"></span>
          <a href="#">chirpline.net/trivc</a><br>tenetur a volup tatibus maiores alias<br><a class="ext" href="#">http://www.incidunt.com/ ut/labore/4et</a><br><span class="actions">2 minutes ago · reply · retweet · favorite</span></div>
      </div>
    </section>

    <section class="latest">
      <h2 class="section-title">Latest News and Evetns</h2>
      <div class="bar" style="width:683px">News<span class="sep">|</span><span class="tab">Stories</span><span class="sep">|</span><span class="tab">Recent</span>
        <span class="arrow"><svg width="8" height="9" viewBox="0 0 8 9"><path d="M2 1l4 3.5L2 8" stroke="#333" stroke-width="1.8" fill="none"/></svg></span>
      </div>
      <div class="grid">
        <div class="card"><span class="thumb" style="background:linear-gradient(#4d7fb8,#8a7a4a)" role="img" aria-label="Runner on a trail at dusk"></span><h4>Nulla placerat pulvinar dui</h4>Ac sodales nunc dictum et. Nunc blandit id leo eu blandit.<div class="date">Jun-17-2013</div></div>
        <div class="card"><span class="thumb" style="background:linear-gradient(#2f6fb3,#1d3f70)" role="img" aria-label="Athlete drinking water"></span><h4>Nulla placerat pulvinar dui</h4>Ac sodales nunc dictum et. Nunc blandit id leo eu blandit.<div class="date">Jun-17-2013</div></div>
        <div class="card"><span class="thumb" style="background:linear-gradient(#6d9ccc,#3a3e44)" role="img" aria-label="Athlete interviewed by press"></span><h4>Nulla placerat pulvinar dui</h4>Ac sodales nunc dictum et. Nunc blandit id leo eu blandit.<div class="date">Jun-17-2013</div></div>
        <div class="card"><span class="thumb" style="background:linear-gradient(#6f8a6a,#a9574a)" role="img" aria-label="Runners on a stadium track"></span><h4>Nulla placerat pulvinar dui</h4>Ac sodales nunc dictum et. Nunc blandit id leo eu blandit.<div class="date">Jun-17-2013</div></div>
        <div class="card"><span class="thumb" style="background:linear-gradient(#b04848,#3c4a78)" role="img" aria-label="Crowd with flags at a race"></span><h4>Nulla placerat pulvinar dui</h4>Ac sodales nunc dictum et. Nunc blandit id leo eu blandit.<div class="date">Jun-17-2013</div></div>
        <div class="card"><span class="thumb" style="background:linear-gradient(#e7ddd0,#c0443c)" role="img" aria-label="Sprinter in starting blocks"></span><h4>Nulla placerat pulvinar dui</h4>Ac sodales nunc dictum et. Nunc blandit id leo eu blandit.<div class="date">Jun-17-2013</div></div>
      </div>
    </section>
  </main>

  <footer class="footer">
    <nav><a href="#">Home</a><span class="pipe">|</span><a href="#">What we do</a><span class="pipe">|</span><a href="#">Athletes</a><span class="pipe">|</span><a href="#">News</a><span class="pipe">|</span><a href="#">Contact Us</a></nav>
    <p class="copy">Copyright &nbsp;© &nbsp;2013 &nbsp;&nbsp; www.lumbrecrest.com &nbsp;&nbsp; All rights reserved.</p>
    <div class="brand-small"><i></i>Lumbre Crest</div>
  </footer>
</div>
</body>
</html>
```